Business card for my company-RMK Design Studio

I do not have a logo-I like red and keeping it clean. Information that should be on the card:
Tom Brakefield AIA
Architecture Planning Interiors
Cell Phone-614.492.5068
email-rmkarchitect1@lunvale.com
www.rmkdesignstudio.net

```html
<!DOCTYPE html>
<html lang="en">
<head>
<meta charset="utf-8">
<title>RMK Design Studio – Business Card</title>
<link href="https://fonts.googleapis.com/css2?family=Jost:wght@300;400;500;700&display=swap" rel="stylesheet">
<style>
  :root {
    --brand-red: #e30022;
    --deep-ground: #1f0006;
    --paper: #ffffff;
    --blush: #f7c9d1;
    --band-grey: #e1e1e1;
    --ink: #2b2b2b;
  }
  * { box-sizing: border-box; margin: 0; padding: 0; }
  html, body {
    width: 1009px; height: 1200px; overflow: hidden;
    background: var(--deep-ground);
    font-family: "Jost", "Futura", sans-serif;
  }
  .sheet {
    position: relative; width: 1009px; height: 1200px;
    display: flex; flex-direction: column; align-items: center; justify-content: center; gap: 64px;
  }
  .card {
    position: relative; width: 800px; height: 458px; overflow: hidden;
  }

  /* front */
  .card--front { background: var(--paper); color: var(--ink); }
  .blush-circle { position: absolute; border-radius: 50%; background: var(--blush); }
  .blush-circle--right { width: 266px; height: 266px; left: 715px; top: 147px; }
  .blush-circle--bottom { width: 316px; height: 316px; left: 417px; top: 375px; }
  .side-tab {
    position: absolute; left: 0; top: 242px; width: 36px; height: 216px;
    background: var(--brand-red); border-radius: 0 36px 0 0;
  }
  .wordmark {
    display: flex; align-items: center; gap: 14px;
    font-weight: 300; font-size: 44px; letter-spacing: 1px; line-height: 1;
    text-transform: uppercase;
  }
  .wordmark__square { width: 30px; height: 30px; background: var(--brand-red); flex: none; }
  .card--front .wordmark { position: absolute; left: 55px; top: 98px; color: var(--ink); }
  .person {
    position: absolute; right: 70px; top: 320px; text-align: right; display: none;
  }
  .holder {
    position: absolute; right: 70px; top: 180px; text-align: right;
  }
  .holder__name { font-size: 38px; font-weight: 700; line-height: 1.05; }
  .holder__name span { font-weight: 500; }
  .holder__role { font-size: 24px; font-weight: 400; }
  .contact-list {
    position: absolute; left: 55px; top: 270px; list-style: none;
    font-size: 24px; line-height: 31px; font-weight: 400;
  }
  .contact-list li { display: flex; align-items: flex-start; gap: 12px; }
  .contact-list svg { flex: none; width: 24px; height: 24px; margin-top: 4px; }

  /* back */
  .card--back { background: var(--brand-red); }
  .card--back .wordmark {
    position: absolute; left: 0; right: 0; top: 205px; justify-content: center;
    color: var(--paper); font-size: 50px;
  }
  .card--back .wordmark__square { background: var(--paper); }
  .url-band {
    position: absolute; left: 0; right: 0; top: 376px; height: 48px;
    background: var(--band-grey); color: var(--brand-red);
    display: flex; align-items: center; justify-content: center;
    font-size: 30px; font-weight: 500; letter-spacing: 7px;
  }
</style>
</head>
<body>
<main class="sheet">

  <section class="card card--front" aria-label="Card front">
    <div class="blush-circle blush-circle--right"></div>
    <div class="blush-circle blush-circle--bottom"></div>
    <div class="side-tab"></div>

    <div class="wordmark"><span class="wordmark__square"></span>RMK Design Studio</div>

    <div class="holder">
      <p class="holder__name">Daniel <span>Hart</span></p>
      <p class="holder__role">Project Manager</p>
    </div>

    <ul class="contact-list">
      <li>
        <svg viewBox="0 0 24 24"><circle cx="12" cy="12" r="12" fill="#e30022"/><path d="M12 5a4.5 4.5 0 0 0-4.5 4.5C7.5 13 12 18 12 18s4.5-5 4.5-8.5A4.5 4.5 0 0 0 12 5z" fill="#fff"/><circle cx="12" cy="9.6" r="1.8" fill="#e30022"/></svg>
        <span>Tom Brakefield AIA<br>Architecture Planning Interiors</span>
      </li>
      <li>
        <svg viewBox="0 0 24 24"><circle cx="12" cy="12" r="12" fill="#e30022"/><path d="M8.2 6.5l2 2.3-1.1 1.5a8 8 0 0 0 4.6 4.6l1.5-1.1 2.3 2-1.2 1.7c-4.6-.3-9.1-4.8-9.4-9.4z" fill="#fff"/></svg>
        <span>614.492.5068</span>
      </li>
      <li>
        <svg viewBox="0 0 24 24"><circle cx="12" cy="12" r="12" fill="#e30022"/><rect x="6" y="8" width="12" height="8.5" rx="1" fill="#fff"/><path d="M6.5 8.6l5.5 4.3 5.5-4.3" fill="none" stroke="#e30022" stroke-width="1.2"/></svg>
        <span>rmkarchitect1@lunvale.com</span>
      </li>
      <li>
        <svg viewBox="0 0 24 24"><circle cx="12" cy="12" r="12" fill="#e30022"/><path d="M8.5 6.5l7.5 6.2-3.3.5 1.9 3.7-1.5.8-1.9-3.7-2.5 2.2z" fill="#fff"/></svg>
        <span>rmkdesignstudio.net</span>
      </li>
    </ul>
  </section>

  <section class="card card--back" aria-label="Card back">
    <div class="wordmark"><span class="wordmark__square"></span>RMK Design Studio</div>
    <div class="url-band">www.rmkdesignstudio.net</div>
  </section>

</main>
</body>
</html>
```